eBook cover for new contemporary fiction

I need a front and back cover design for my newly finished ebook. It is entitled "Paper Crown". The following should help in understanding the story line:
Back Cover blurb:

Dale and Rhoda Pembury ran a successful courier company-until the Internet changed the way documents were delivered. Now, through a series of tragic events and poor financial decisions, Dale has begun to ask himself some tough questions.

To what length would Dale go to save himself from the effects of poor financial decisions? How far can he sink to hide personal failure from his wife and children? Could he burn his house down to collect insurance? Could he fake his own death to give his family what they deserve? Or could he even kill his wife and children to end their struggles?

While Dale is trapped in his own personal hell, Rhoda discovers what she thinks may be an anodyne for their financial ailments. Can it save them in time? Or will it destroy them all?

Written by an experienced (now reformed) telemarketer, the insidious greed and trickery of the industry is revealed in a story that will find you grinding your teeth and clenching your jaw. Not only is Paper Crown entertaining, but it is a welcome manifesto of true confessions by a former insider of the industry.

(end of back cover)

PLEASE NOTE: I have received a number of decent submissions but they are all missing the emotions behind what I need. I wrote this to one of the artists, perhaps it will help you:
I have really been trying to digest your cover art and what it is I'm trying to portray. I still like this design but have finally identified what it is that has kept me uneasy about it. The guy you have on the cover doesn't fit the image of the protagonist. There is a disconnect that I cannot not reconcile in my my mind. In the book, the salesman rides a Vantor and drives a convertible Delvane. He is a womanizer and an admitted alcoholic, though thrives on both. He is very good at what he does and is continually driven to achieve more. The reason I liked the caricature of the sample art I posted is that it shows sleazy class. It portrays the slickness of a master manipulator. Having said that, I am not convinced that this cover has to have "someone" to portray all the things I have just mentioned. Am I making any sense?

I really want to portray Greed, Lust, and Fear - or at least two out of the three. Displaying the bottle of Paper Crown certainly represents the greed but I don't get a sense of what the book is about. You are probably too busy, but did you read the sample chapters? There is real heartache and tragedy in a family and the salesman attempts to exploit that.

Let me know what you think of all this. Thanks for listening.

END NOTE

Also, if you are so inclined, there are 9 chapters at PaperCrownTheBook.test that will give you a great understanding of what the cover needs to portray. (The site is under development but the chapters are there to read.)

This is my first use of ArtQuorum and as such I am sure I have not given you all the information you need. Please do not hesitate to ask. I will respond as quickly as I can.

The authors name should appear as Warren T. Ashby.

40 year-olds and up, both male and female.

Financial

• The specs must satisfy Borealis Leaf requirements for ebook covers.
The title of: Paper Crown
The author's name of: Warren T. Ashby
The tagline of: A Modern Tale of Greed, Lust, and Fear
• Purely informational: the attached file is a cover I had put together from artwork I found on the Internet. I tracked the artist down to discover that the piece had been commissioned for another company and is not available. However, I love the color, the imagery, the depth of message within the art. I am going at this project with an open mind, the sample is just one that I loved. (Please note the author's name on this sample is not as it should be displayed in your rendering.)

```html
<!DOCTYPE html>
<html lang="en">
<head>
<meta charset="utf-8">
<title>Paper Crown — Cover Wrap</title>
<link rel="stylesheet" href="https://fonts.googleapis.com/css2?family=Cinzel:wght@400;700&family=Six+Caps&display=swap">
<style>
  :root {
    --wood-green: #3f5a1c;
    --wood-olive: #6d6a1c;
    --wood-amber: #a8641a;
    --wood-rust: #8a3a10;
    --spine-dark: #1d2a12;
    --spine-edge: #2f7a2a;
    --ink-light: #f2efe2;
    --spine-cream: #e9d7a4;
    --tagline-orange: #e8902e;
    --credit-band: rgba(20, 20, 14, 0.75);
  }
  html, body {
    margin: 0;
    padding: 0;
    width: 1200px;
    height: 900px;
    overflow: hidden;
    background: #111;
  }
  .cover-wrap {
    position: relative;
    width: 1200px;
    height: 900px;
    overflow: hidden;
    font-family: "Cinzel", serif;
    color: var(--ink-light);
  }
  .back-cover, .front-cover {
    position: absolute;
    top: 0;
    height: 900px;
  }
  .back-cover {
    left: 0;
    width: 548px;
    background:
      radial-gradient(ellipse at 40% 55%, rgba(190,120,30,0.55), transparent 60%),
      linear-gradient(180deg, #233a14 0%, var(--wood-green) 30%, var(--wood-olive) 55%, var(--wood-amber) 75%, #3a2e10 100%);
  }
  .front-cover {
    left: 648px;
    width: 552px;
    background:
      radial-gradient(ellipse at 80% 70%, rgba(190,80,20,0.6), transparent 60%),
      linear-gradient(180deg, rgba(10,14,6,0.55) 0%, transparent 20%),
      linear-gradient(100deg, #2a3d14 0%, var(--wood-olive) 35%, var(--wood-amber) 70%, var(--wood-rust) 100%);
  }
  .spine {
    position: absolute;
    left: 548px;
    top: 0;
    width: 100px;
    height: 900px;
    background: linear-gradient(90deg, #152010, var(--spine-dark) 50%, #152010);
    border-top: 8px solid var(--spine-edge);
    box-sizing: border-box;
    overflow: hidden;
  }
  .spine-title, .spine-author {
    position: absolute;
    left: 50%;
    writing-mode: vertical-rl;
    transform: translateX(-50%);
    white-space: nowrap;
  }
  .spine-title {
    top: 58px;
    font-family: "Six Caps", sans-serif;
    font-size: 96px;
    line-height: 1;
    letter-spacing: 6px;
    background: linear-gradient(90deg, #6fd06a, #e0c070, #d0501c);
    -webkit-background-clip: text;
    background-clip: text;
    -webkit-text-fill-color: transparent;
  }
  .spine-author {
    top: 462px;
    font-size: 34px;
    letter-spacing: 2px;
    color: var(--spine-cream);
  }
  .blurb {
    position: absolute;
    left: 48px;
    top: 50px;
    width: 470px;
  }
  .blurb p {
    margin: 0 0 30px;
    font-size: 15px;
    line-height: 20px;
    letter-spacing: 2.4px;
    text-transform: uppercase;
    text-align: justify;
    text-align-last: left;
  }
  .author-note {
    position: absolute;
    left: 38px;
    width: 486px;
    top: 566px;
    margin: 0;
    font-size: 12.4px;
    line-height: 22px;
    letter-spacing: 1px;
    text-transform: uppercase;
    text-align: justify;
    text-align-last: center;
  }
  .credit-band {
    position: absolute;
    left: 20px;
    top: 765px;
    width: 510px;
    height: 88px;
    background: var(--credit-band);
  }
  .credit-lines {
    position: absolute;
    right: 188px;
    top: 10px;
    margin: 0;
    text-align: right;
    font-size: 10.5px;
    line-height: 18px;
    letter-spacing: 1.5px;
    text-transform: uppercase;
  }
  .pub-lines {
    position: absolute;
    left: 2px;
    top: 58px;
    margin: 0;
    font-size: 10px;
    line-height: 13px;
    letter-spacing: 1.2px;
    text-transform: uppercase;
  }
  .pub-lines .price { margin-left: 10px; }
  .isbn-space {
    position: absolute;
    left: 357px;
    top: 765px;
    width: 171px;
    height: 87px;
    background: #fff;
  }
  .site-address {
    position: absolute;
    left: 0;
    width: 556px;
    top: 866px;
    text-align: center;
    font-size: 12px;
    letter-spacing: 2.5px;
    text-transform: uppercase;
  }
  .front-art, .front-type { position: absolute; left: 0; top: 0; }
  .tagline {
    position: absolute;
    left: 0;
    width: 552px;
    top: 803px;
    margin: 0;
    text-align: center;
    font-size: 25px;
    line-height: 34px;
    letter-spacing: 1px;
    font-weight: 700;
    color: var(--tagline-orange);
  }
</style>
</head>
<body>
<main class="cover-wrap">

  <section class="back-cover" aria-label="Back cover">
    <div class="blurb">
      <p>Dale and Rhoda Pembury ran a successful courier company-until the Internet changed the way documents were delivered. Now, through a series of tragic events and poor financial decisions, Dale has begun to ask himself some tough questions.</p>
      <p>To what length would Dale go to save himself from the effects of poor financial decisions? How far can he sink to hide personal failure from his wife and children? Could he burn his house down to collect insurance? Could he fake his own death to give his family what they deserve? Or could he even kill his wife and children to end their struggles?</p>
      <p>While Dale is trapped in his own personal hell, Rhoda discovers what she thinks may be an anodyne for their financial ailments. Can it save them in time? Or will it destroy them all?</p>
    </div>

    <p class="author-note">Written by an experienced (now reformed) telemarketer, the insidious greed and trickery of the industry is revealed in a story that will find you grinding your teeth and clenching your jaw.<br>Not only is Paper Crown entertaining, but it is a welcome manifesto of true confessions by a former insider of the industry.</p>

    <div class="credit-band">
      <p class="credit-lines">Written by Warren T. Ashby<br>Published by Warren T. Ashby</p>
      <p class="pub-lines">Published 2013<br>Cover design by Colin Marsh <span class="price">R.R.P $6.95</span></p>
    </div>
    <div class="isbn-space"></div>
    <div class="site-address">PaperCrownTheBook.test</div>
  </section>

  <section class="spine" aria-label="Spine">
    <div class="spine-title">PAPER CROWN</div>
    <div class="spine-author">WARREN T. ASHBY</div>
  </section>

  <section class="front-cover" aria-label="Front cover">
    <svg class="front-art" width="552" height="900" viewBox="0 0 552 900">
      <defs>
        <radialGradient id="still-life-tones" cx="0.55" cy="0.45" r="0.6">
          <stop offset="0" stop-color="#5f7f62" stop-opacity="0.55"/>
          <stop offset="0.55" stop-color="#7a3a18" stop-opacity="0.3"/>
          <stop offset="1" stop-color="#7a3a18" stop-opacity="0"/>
        </radialGradient>
      </defs>
      <rect role="img" aria-label="Still life on wood: a tipped-over green tonic bottle spilling a red stain, beside a crumpled banknote and a red lipstick" x="60" y="100" width="440" height="470" fill="url(#still-life-tones)"/>
    </svg>

    <svg class="front-type" width="552" height="900" viewBox="0 0 552 900">
      <defs>
        <linearGradient id="author-metal" x1="0" y1="0" x2="0" y2="1">
          <stop offset="0" stop-color="#7fe6b0"/>
          <stop offset="1" stop-color="#2f9a5e"/>
        </linearGradient>
        <linearGradient id="title-metal" x1="0" y1="0" x2="0" y2="1">
          <stop offset="0" stop-color="#5fd06a"/>
          <stop offset="0.45" stop-color="#cfd6c0"/>
          <stop offset="0.7" stop-color="#d88a3a"/>
          <stop offset="1" stop-color="#c8401a"/>
        </linearGradient>
      </defs>
      <text x="18" y="92" font-family="Six Caps, sans-serif" font-size="96" letter-spacing="6" textLength="516" lengthAdjust="spacingAndGlyphs" fill="url(#author-metal)">WARREN T. ASHBY</text>
      <text x="12" y="790" font-family="Six Caps, sans-serif" font-size="280" textLength="528" lengthAdjust="spacingAndGlyphs" fill="url(#title-metal)" stroke="#1a2a10" stroke-width="2">PAPER CROWN</text>
    </svg>

    <p class="tagline">A Modern Tale of Greed,<br>Lust, and Fear</p>
  </section>

</main>
</body>
</html>
```